Plumhart honey labels

we are in need of new labels. we are changing to shorter round cream style honey jars. scalable from 25-100mm tall. We are looking for simple yet elegant
we sell premium varietal honeys from around the USA and locally produced small batch honeys. we are in San Francisco and Sonoma county Calif. for 10 yrs. we strive to supply only the highest quality honey at a premium price point
our logo is gold text on black background, can be found at plumhart.net

Reason: would like to see more designs for a paper wrap around label

Reason: get your designs in so we can choose soon

Target Market(s)

we provide Premium honeys that cannot be found easily elsewhere
at Premium prices. Our customers are socially aware but not afraid to pay more for a premium product

Colors

Designer to choose colors to be used in the design.

Requirements
Must have
• we will be using round jars in 3 sizes, 1.5-4 inches tall, 53mm,63mm,89mm diameter
all will have black lids
will need wrap around labels for labeling machine application
will need simple nutrition label info included
Nice to have
• room on side for nutrition label info
plumhart logo included, of course
space on side for short description of honey
Should not have
• honey dripping off honey dipper or spoon
picture of honeycomb
comic bees or flowers

```html
<!DOCTYPE html>
<html lang="en">
<head>
<meta charset="utf-8">
<title>Plumhart Honey – Wrap Label</title>
<link rel="stylesheet" href="https://fonts.googleapis.com/css2?family=Arimo:ital,wght@0,400;0,700;1,400;1,700&family=Lobster&display=swap">
<style>
  :root {
    --bg: #d4d4d4;
    --cream: #fcf1c6;
    --brown: #7a4816;
    --ink: #151515;
    --comb-light: #fbef9f;
    --comb-deep: #f5e06a;
    --gold: #d9a441;
    --white: #ffffff;
  }
  * { margin: 0; padding: 0; box-sizing: border-box; }
  html, body { width: 1200px; height: 1043px; overflow: hidden; background: var(--bg); }
  body { position: relative; font-family: "Arimo", Arial, sans-serif; color: var(--ink); }

  .label {
    position: absolute; left: 40px; top: 274px; width: 1120px; height: 495px;
    background: var(--cream);
    box-shadow: 0 6px 18px rgba(0,0,0,0.25);
  }

  /* description panel */
  .description {
    position: absolute; left: 16px; top: 92px; width: 326px; height: 338px;
    border: 1.5px solid var(--brown); background: var(--cream);
  }
  .description__text {
    padding: 16px 18px; font-size: 14px; line-height: 1.25;
  }
  .description__text strong { font-weight: 700; }
  .storage {
    position: absolute; left: 0; right: 0; bottom: 0; height: 68px;
    background: var(--brown); color: var(--white); text-align: center;
    font-style: italic; padding-top: 10px;
  }
  .storage__title { font-weight: 700; font-size: 17px; }
  .storage__note { font-size: 14px; line-height: 1.15; }

  .footer-left {
    position: absolute; left: 26px; top: 446px; display: flex; align-items: center; gap: 18px;
  }
  .website { font-weight: 700; font-size: 17px; margin-left: 10px; }

  /* centre brand */
  .brand {
    position: absolute; left: 480px; top: 118px; display: flex; align-items: center; gap: 12px;
  }
  .brand__dot { width: 18px; height: 18px; border-radius: 50%; background: var(--gold); }
  .brand__name { font-family: "Lobster", cursive; font-size: 50px; color: var(--brown); }

  .product-title {
    position: absolute; left: 372px; width: 550px; top: 278px; text-align: center;
    font-family: "Lobster", cursive; font-size: 64px; color: var(--brown); line-height: 1;
  }
  .origin-bar {
    position: absolute; left: 362px; top: 372px; width: 563px; height: 40px;
    background: var(--brown); color: var(--white);
    font-weight: 700; font-size: 20px; text-align: right; padding: 8px 22px 0 0;
  }
  .comb-field {
    position: absolute; left: 362px; top: 412px; width: 563px; height: 83px;
    background: linear-gradient(90deg, var(--comb-light), var(--comb-deep) 50%, var(--comb-light));
  }
  .net-weight {
    position: absolute; right: 200px; top: 432px; text-align: right;
    font-weight: 700; font-size: 18px; line-height: 1.2;
  }

  /* nutrition panel */
  .nutrition {
    position: absolute; left: 930px; top: 38px; width: 170px;
    border: 1.5px solid var(--ink); padding: 4px 6px; font-size: 12px; line-height: 1.2;
    background: var(--cream);
  }
  .nutrition__title { font-weight: 700; font-size: 22px; line-height: 1; }
  .nutrition__rule-thick { height: 10px; background: var(--ink); margin: 3px 0; }
  .nutrition__rule-mid { height: 5px; background: var(--ink); margin: 3px 0; }
  .nutrition__row { display: flex; justify-content: space-between; border-top: 1px solid var(--ink); padding: 2px 0; }
  .nutrition__row b { font-weight: 700; }
  .nutrition__row--indent { padding-left: 10px; }
  .nutrition__small { font-size: 9px; font-weight: 700; }
  .nutrition__dv { text-align: right; font-size: 9px; font-weight: 700; }
  .nutrition__foot { font-size: 9px; line-height: 1.15; padding-top: 2px; }

  .producer {
    position: absolute; left: 940px; top: 378px; font-size: 14px; line-height: 1.25;
  }
  .producer b { font-weight: 700; font-size: 15px; }
</style>
</head>
<body>
  <div class="label">
    <section class="description">
      <p class="description__text"><strong>Description here...</strong> we sell premium varietal honeys from around the USA and locally produced small batch honeys. we are in San Francisco and Sonoma county Calif. for 10 yrs. we strive to supply only the highest quality honey at a premium price point</p>
      <div class="storage">
        <div class="storage__title">Store at room temperature.</div>
        <div class="storage__note">If honey solidifies, gently<br>heat jars to reliquify.</div>
      </div>
    </section>

    <div class="footer-left">
      <svg width="26" height="30" viewBox="0 0 26 30" aria-label="Dispose responsibly">
        <circle cx="6" cy="4" r="3" fill="#151515"/>
        <path d="M4 8 L2 18 L5 18 L7 10 Z" fill="#151515"/>
        <rect x="11" y="12" width="12" height="16" fill="#151515"/>
        <rect x="10" y="10" width="14" height="2" fill="#151515"/>
      </svg>
      <svg width="34" height="32" viewBox="0 0 34 32" aria-label="Recycling mark">
        <polygon points="17,2 32,29 2,29" fill="none" stroke="#151515" stroke-width="2.5"/>
      </svg>
      <span class="website">WWW.PLUMHART.NET</span>
    </div>

    <div class="brand">
      <span class="brand__dot"></span>
      <span class="brand__name">plumhart</span>
    </div>

    <h1 class="product-title">Plumhart Honey</h1>
    <div class="origin-bar">Sebastopol &amp; San Francisco</div>
    <div class="comb-field" role="img" aria-label="Soft honeycomb-toned background pattern"></div>
    <div class="net-weight">NET WT.<br>30 lbs (70g)</div>

    <aside class="nutrition">
      <div class="nutrition__title">Nutrition Facts</div>
      <div>Serving Size 1 Tbsp (21g)</div>
      <div>Servings Per Container 00</div>
      <div class="nutrition__rule-thick"></div>
      <div class="nutrition__small">Amount Per Serving</div>
      <div class="nutrition__row"><b>Calories 60</b></div>
      <div class="nutrition__rule-mid"></div>
      <div class="nutrition__dv">%Daily Value*</div>
      <div class="nutrition__row"><span><b>Total Fat</b> 0g</span><b>0%</b></div>
      <div class="nutrition__row"><span><b>Sodium</b> 0mg</span><b>0%</b></div>
      <div class="nutrition__row"><span><b>Total Carb.</b> 17g</span><b>6%</b></div>
      <div class="nutrition__row nutrition__row--indent"><span>Sugars 16g</span></div>
      <div class="nutrition__row"><span><b>Protein</b> 0g</span><b>0%</b></div>
      <div class="nutrition__rule-thick"></div>
      <div class="nutrition__foot">*Percent Daily Values (DV) are based on 2,000 calorie diet.</div>
    </aside>

    <div class="producer">
      <b>Plumhart</b><br>
      123 Address, City<br>
      <b>Product of USA</b>
    </div>
  </div>
</body>
</html>
```